Redesign of page from emergency manual

Please redesign this PDF to look better. Please don't include any stock photos. It must be legible. Making some words bold is probably a good idea.

Here are some things I like :

https://tarrowbooks.com.au/collections/frontpage/products/the-plk-v2-ebook

https://img-cd.vostramediafiles.com/qa-ejkwPLOTYY_SuCKbZNu411Qwgjv8YssPxEdzXN93hDkSRjLXK8WmfgbmrJW4ZZ3yUPK=w1052-h592-rw

```html
<!DOCTYPE html>
<html lang="en">
<head>
<meta charset="utf-8">
<title>Hypertension, Acute</title>
<link rel="stylesheet" href="https://fonts.googleapis.com/css2?family=Poppins:wght@400;500;600;700;800&display=swap">
<style>
:root{
  --blue:#0767a8;
  --cyan:#67e8fb;
  --cyan-dark:#52c5d8;
  --ink:#1b1b1b;
  --panel:#f2f2f2;
  --rule:#c9c9c9;
  --page:#e6e6e6;
  --white:#ffffff;
}
*{box-sizing:border-box;margin:0;padding:0}
html,body{width:1200px;height:1034px;overflow:hidden;background:var(--page);font-family:'Poppins',sans-serif;color:var(--ink)}
.card{position:absolute;left:17px;top:67px;width:1166px;height:900px;background:var(--white);overflow:hidden}
.card > *{position:absolute}
.header-band{left:0;top:0}
.title{left:37px;top:14px;font-size:82px;font-weight:700;color:var(--white);letter-spacing:1px;line-height:1.1}
.subtitle{left:40px;top:100px;font-size:25px;font-weight:600;color:var(--white)}
.sidebar{left:1100px;top:0;width:66px;height:900px;background:var(--cyan)}
.page-no{left:1100px;width:66px;top:28px;text-align:center;font-size:32px;font-weight:700;color:var(--blue)}
.side-title{left:1133px;top:235px;transform-origin:0 0;transform:rotate(90deg) translateY(-50%);font-size:34px;font-weight:700;color:var(--blue);white-space:nowrap}
.revision{left:1133px;top:735px;transform-origin:0 0;transform:rotate(90deg) translateY(-50%);font-size:12px;font-weight:600;color:var(--ink);white-space:nowrap}
.intro{left:40px;top:166px;width:540px;font-size:14.5px;line-height:1.25}
.intro ul{list-style:none}
.intro li{position:relative}
.dot::before{content:"";position:absolute;width:6px;height:6px;border-radius:50%;background:var(--blue)}
.intro .lead{padding-left:26px;margin-left:0}
.intro .lead::before{left:3px;top:4px;background:var(--cyan)}
.intro .sub{margin:20px 0 0 44px;padding-left:0}
.intro .sub::before{left:-16px;top:6px}
.intro .subsub{margin:14px 0 0 58px}
.intro .subsub::before{content:"–";position:absolute;left:-10px;color:var(--cyan-dark)}
.caution{margin-top:10px}
.caution b{color:var(--blue);font-weight:700}
.range{left:594px;top:170px;width:485px;height:256px;background:var(--blue);border-radius:6px}
.range h2{position:absolute;left:17px;top:10px;font-size:23px;font-weight:700;color:var(--white)}
.range table{position:absolute;left:18px;top:47px;width:448px;border-collapse:collapse;background:var(--white);border-radius:6px;overflow:hidden}
.range th{height:34px;font-size:19px;font-weight:600;background:var(--cyan);color:var(--ink)}
.range th.mid{background:var(--cyan-dark)}
.range td{text-align:center;font-size:14.5px;border-right:1px solid var(--rule);border-top:1px solid var(--rule);height:55px}
.range tr:last-child td{height:45px}
.range td:last-child{border-right:none}
.range tr:nth-child(2) td{border-top:none}
.head{top:442px;height:42px;background:var(--blue);color:var(--white);font-size:19px;font-weight:600;text-align:center;line-height:40px;border-radius:5px 5px 0 0}
.body{top:484px;height:246px;background:var(--panel);border-radius:0 0 6px 6px}
.action-col{left:40px;width:304px}
.drug-col{left:351px;width:726px}
.row{position:absolute;left:0;right:0;border-bottom:1px solid var(--rule);font-size:14.5px}
.row:last-child{border-bottom:none}
.action-col .row{padding-left:29px}
.drug-col ul{list-style:none;padding-left:64px}
.drug-col li{position:relative;line-height:23px}
.drug-col li::before{left:-16px;top:8px}
.differential{left:41px;top:745px;width:1059px;height:42px;background:var(--cyan)}
.differential h3{position:absolute;left:16px;top:3px;font-size:26px;font-weight:700;color:var(--ink);letter-spacing:.3px}
.diff-col{top:798px;list-style:none;font-size:14.5px;line-height:1.25}
.diff-col li{position:relative;padding-left:16px;margin-bottom:9px}
.diff-col li::before{left:0;top:6px}
</style>
</head>
<body>
<main class="card">
  <svg class="header-band" width="1045" height="152" viewBox="0 0 1045 152" aria-hidden="true"><polygon points="0,0 1041,0 1010,151 0,151" fill="#0767a8"/></svg>
  <h1 class="title">HYPERTENSION, ACUTE</h1>
  <p class="subtitle">Sustained high blood pressure refractory to treating reversible causes</p>

  <div class="sidebar"></div>
  <div class="page-no">12</div>
  <div class="side-title">Hypertension, Acute</div>
  <div class="revision">Revision Feb 2020</div>

  <section class="intro">
    <ul>
      <li class="lead dot">In pediatrics, hypertension is almost always treated by addressing likely causes such as light anesthesia or measurement error:</li>
      <li class="sub dot">Ensure correct BP cuff size: cuff bladder<br>width ~ 40% of limb circumference</li>
      <li class="sub dot">Ensure arterial line transducer is at level of heart</li>
      <li class="subsub">Consider placing arterial line if not already present</li>
    </ul>
    <p class="caution"><b>* CAUTION:</b> Anti-hypertensive drugs are almost never needed for routine pediatric cases. These medications are used almost exclusively for specialized cardiac, neurosurgical, or endocrine (pheochromocytoma) cases. Consult an expert before use. Rule-out increased ICP.</p>
  </section>

  <section class="range">
    <h2>Hypertensive Blood Pressure Range*</h2>
    <table>
      <tr><th>Age (yr)</th><th class="mid">Systolic</th><th>Diastolic</th></tr>
      <tr><td>newborn</td><td>&gt;97</td><td>&gt;70</td></tr>
      <tr><td>1-3</td><td>&gt;105</td><td>&gt;61</td></tr>
      <tr><td>4-12</td><td>&gt;113</td><td>&gt;86</td></tr>
    </table>
  </section>

  <div class="head action-col">Action</div>
  <div class="head drug-col">Drug (IV Dosing)</div>
  <div class="body action-col">
    <div class="row" style="top:0;height:77px;padding-top:18px">Direct smooth muscle relaxation</div>
    <div class="row" style="top:77px;height:59px;padding-top:16px">β-Adrenergic blockade</div>
    <div class="row" style="top:136px;height:59px;padding-top:13px;font-size:13.5px">Calcium channel blockade</div>
    <div class="row" style="top:195px;height:51px;padding-top:12px;font-size:13.5px">D1-dopamine agonist</div>
  </div>
  <div class="body drug-col">
    <div class="row" style="top:0;height:77px;padding-top:18px"><ul><li class="dot">Sodium nitroprusside 0.5-10 MICROgrams/kg/min</li><li class="dot">HydrALAZINE 0.1-0.2 mg/kg (adult dose 5-10 mg)</li></ul></div>
    <div class="row" style="top:77px;height:59px;padding-top:6px"><ul><li class="dot">Esmolol 100-500 MICROgrams/kg over 5 min, then 25-300 MICROgrams/kg/min</li><li class="dot">Labetalol (also α effect) 0.2-1 mg/kg q 10 min; 0.4-3 mg/kg/hour (infusion)</li></ul></div>
    <div class="row" style="top:136px;height:59px;padding-top:6px"><ul><li class="dot">niCARdapine 0.5-5 MICROgrams/kg/min</li><li class="dot">Clevidipine 0.5-3.5 MICROgrams/kg/min</li></ul></div>
    <div class="row" style="top:195px;height:51px;padding-top:12px"><ul><li class="dot">Fenoldopam 0.2-0.8 MICROgrams/kg/min</li></ul></div>
  </div>

  <div class="differential"><h3>CONSIDER DIFFERENTIAL (PARTIAL)</h3></div>
  <ul class="diff-col" style="left:60px;width:380px">
    <li class="dot">Light anesthesia (consider vaporizer or infusion pump empty or malfunctioning)</li>
    <li class="dot">Hypercarbia</li>
  </ul>
  <ul class="diff-col" style="left:465px;width:420px">
    <li class="dot" style="margin-bottom:8px">Hypoxemia</li>
    <li class="dot" style="margin-bottom:8px">Arterial line transducer too low or BP cuff too small</li>
    <li class="dot">Withdrawal (EtOH or opioid)</li>
  </ul>
  <ul class="diff-col" style="left:905px;width:190px">
    <li class="dot" style="margin-bottom:8px">Thyroid Storm</li>
    <li class="dot" style="margin-bottom:8px">Pheochromocytoma</li>
    <li class="dot">Drug Error</li>
  </ul>
</main>
</body>
</html>
```